Business Card Design Project

Corvexa logo will be provided after
Front

Ned Marrowick- Construction Manager

Ph: (61) 07 53182079
nmarrowick@corvexa-example.com.au
PO Box 83 Kelvorin 4619

Back
Corvexa
EPCM

Oil - Gas - Mining

Industry/Entity Type

Business

Font styles to use
Sans Serif

Colors
faa54b

Requirements
Must have
• White Back Ground

```html
<!DOCTYPE html>
<html lang="en">
<head>
<meta charset="utf-8">
<title>Corvexa Business Card</title>
<link href="https://fonts.googleapis.com/css2?family=Arimo:wght@400;700&display=swap" rel="stylesheet">
<style>
  :root {
    --backdrop: #e9e6e2;
    --card: #ffffff;
    --ink: #111111;
    --accent: #faa54b;
    --band: #000000;
    --muted: #222222;
  }
  * { box-sizing: border-box; margin: 0; padding: 0; }
  html, body {
    width: 1200px; height: 914px; overflow: hidden;
    background: var(--backdrop);
    font-family: "Arimo", Arial, sans-serif;
    color: var(--ink);
  }
  .canvas {
    position: relative; width: 1200px; height: 914px;
  }
  .card {
    position: absolute; left: 270px;
    width: 660px; height: 377px;
    background: var(--card);
    overflow: hidden;
    box-shadow: 0 6px 18px rgba(0,0,0,0.18);
  }
  .card--front { top: 50px; }
  .card--back { top: 487px; }

  .wordmark {
    position: absolute;
    font-weight: 700;
    letter-spacing: 3px;
    color: var(--ink);
    text-transform: uppercase;
  }
  .card--front .wordmark { left: 270px; top: 34px; font-size: 44px; }

  .holder { position: absolute; left: 44px; top: 112px; }
  .holder__name { font-size: 36px; font-weight: 400; line-height: 1; }
  .holder__role { font-size: 15px; color: var(--accent); margin-top: 6px; }

  .wave { position: absolute; left: 0; top: 0; width: 660px; height: 377px; }

  .contact {
    position: absolute; left: 360px; top: 208px;
    list-style: none; font-size: 17px; color: var(--muted);
  }
  .contact__item { display: flex; align-items: center; height: 30px; }
  .contact__icon {
    width: 20px; height: 20px; margin-right: 14px;
    background: var(--accent);
    display: flex; align-items: center; justify-content: center;
  }
  .contact__icon svg { width: 13px; height: 13px; }

  .back-lockup {
    position: absolute; left: 0; right: 0; top: 110px;
    text-align: center;
  }
  .card--back .wordmark { position: static; font-size: 52px; display: block; }
  .back-lockup__sectors { font-size: 20px; margin-top: 16px; }
  .back-lockup__service { font-size: 20px; margin-top: 8px; }
</style>
</head>
<body>
<main class="canvas">

  <section class="card card--front" aria-label="Card front">
    <svg class="wave" viewBox="0 0 660 377" aria-hidden="true">
      <path d="M0 208 C120 222 230 300 360 318 C470 334 560 326 660 322 L660 377 L0 377 Z" fill="var(--band)"/>
      <path d="M0 190 C110 200 200 275 320 300 C250 282 150 220 0 200 Z" fill="var(--accent)"/>
    </svg>

    <span class="wordmark">Corvexa</span>

    <div class="holder">
      <h1 class="holder__name">Ned Marrowick</h1>
      <p class="holder__role">Construction Manager</p>
    </div>

    <ul class="contact">
      <li class="contact__item">
        <span class="contact__icon">
          <svg viewBox="0 0 16 16"><path d="M3 2h3l1 3-2 1a8 8 0 0 0 5 5l1-2 3 1v3a1 1 0 0 1-1 1A12 12 0 0 1 2 3a1 1 0 0 1 1-1z" fill="#000"/></svg>
        </span>(61) 07 53182079
      </li>
      <li class="contact__item">
        <span class="contact__icon">
          <svg viewBox="0 0 16 16"><rect x="1" y="3" width="14" height="10" fill="#000"/><path d="M1 3l7 6 7-6" stroke="#faa54b" stroke-width="1.4" fill="none"/></svg>
        </span>nmarrowick@corvexa-example.com.au
      </li>
      <li class="contact__item">
        <span class="contact__icon">
          <svg viewBox="0 0 16 16"><path d="M8 1l7 7h-2v7H9v-4H7v4H3V8H1z" fill="#000"/></svg>
        </span>PO Box 83 Kelvorin 4619
      </li>
    </ul>
  </section>

  <section class="card card--back" aria-label="Card back">
    <div class="back-lockup">
      <span class="wordmark">Corvexa</span>
      <p class="back-lockup__sectors">Oil - Gas - Mining</p>
      <p class="back-lockup__service">EPCM</p>
    </div>
  </section>

</main>
</body>
</html>
```